Web application design for investigative software

ThreadKove is an investigation web application that would organize, create visualizations and allow collaboration. It’s available to anyone and can be used by students, historians, watchdog groups, civic hackers, investigative reporters, mystery enthusiasts, authors, even conspiracy theorists.

We are looking for two related pages. The first, a splash, or front, page and the second a ‘template’ for the web application. They should both be styled the same. The only restriction is that the logo is set.

The design should also be modern and visually well organized — employing a combination of visual devices and info graphics. Keep it light and not too heavy but strong/ professional. Do not be influenced by the current colors of threadkove.example, though the colors should be compatible with the logo..

The pages should be compatible with bootstrap, mostly for it’s JS and component functionality. It can be advised by the designer that a subset of bootstrap be used.

The splash page.
Something along the lines of (though not a copy of) :
https://www.brimloft.example/advertise
http://www.palvornhosting.example/
http://www.murkelsoft.example/
http://www.vontasky.example/

I have a very rough wire frame ish html file uploaded. Use a a guide, but alternate ideas are encouraged.

The application page should have some sort of bar for at the top for system level links a header and a footer. A vertical column to the left between the header and footer for ads, though this will be dynamic as a user can pay out of seeing adds. All dynamic actions will be made by the developers at ThreadKove.

WARNING. Please do not submit pre-made templates from some template website. We can do that ourselves for free.

This project will deliver CODE. HTML, CSS and supporting graphics and files.

```html
<!DOCTYPE html>
<html lang="en">
<head>
<meta charset="utf-8">
<title>ThreadKove – Investigation Web Application</title>
<link href="https://fonts.googleapis.com/css2?family=Signika:wght@400;600;700&family=Cabin+Condensed:wght@400;600&display=swap" rel="stylesheet">
<style>
:root{
  --red:#d8321c;
  --red-dark:#b5230f;
  --ink:#2b2b2b;
  --body:#474747;
  --muted:#8a8a8a;
  --white:#ffffff;
  --footer:#333335;
  --head:"Signika",sans-serif;
  --text:"Cabin Condensed",sans-serif;
}
*{box-sizing:border-box;margin:0;padding:0}
html,body{width:714px;height:1200px;overflow:hidden;background:var(--white)}
body{font-family:var(--text);color:var(--body)}
.page{position:relative;width:714px;height:1200px;overflow:hidden}
.abs{position:absolute}
a{color:inherit;text-decoration:none}

/* header */
.topline{left:0;top:0;width:714px;height:3px;background:var(--red)}
.header{left:0;top:3px;width:714px;height:49px;background:linear-gradient(#fbfbfb,#ececec);border-bottom:1px solid #d9d9d9}
.brand{left:84px;top:13px;display:flex;align-items:center;gap:6px;font-family:var(--head);font-weight:600;font-size:20px;color:var(--red)}
.brand-dot{width:24px;height:24px;border-radius:50%;background:var(--ink)}
.search{left:430px;top:12px;width:155px;height:17px;background:#fff;border:1px solid #ddd;font-size:8px;color:#aaa;padding:3px 5px}
.search svg{position:absolute;right:4px;top:2px}
.account{left:595px;top:12px;font-size:9px;color:var(--ink)}
.account span{color:#999;margin:0 3px}
.nav{left:428px;top:36px;width:223px;display:flex;justify-content:space-between;font-size:8.8px;color:var(--ink)}
.nav a{padding-left:9px;border-left:1px solid #ccc}
.nav a:first-child{border-left:0;padding-left:0}

/* hero */
.hero{left:0;top:52px;width:714px;height:245px;background:linear-gradient(100deg,#1e2230 0%,#2c3140 45%,#4a4d57 70%,#2b2e37 100%)}
.hero-title{left:82px;top:110px;font-family:var(--head);font-weight:600;font-size:25px;line-height:31px;color:var(--white);letter-spacing:.3px}
.hero-copy{left:84px;top:176px;width:210px;font-size:9.5px;line-height:12px;color:#eee}
.btn-hero{left:85px;top:222px;width:121px;height:23px;background:linear-gradient(var(--red),var(--red-dark));color:#fff;font-size:9.5px;font-weight:600;text-align:center;line-height:23px;border-radius:2px}
.dots{left:88px;top:277px;display:flex;gap:3px}
.dots i{width:8px;height:8px;border-radius:50%;background:#222;display:block}
.dots i:first-child{background:var(--red)}
.arrow-l{left:24px;top:150px}
.arrow-r{left:672px;top:150px}

/* features */
.features{left:0;top:297px;width:714px;height:213px;background:linear-gradient(#f3f3f3,#fafafa 60%,#fff)}
.feature{top:326px;width:166px;text-align:center}
.feature h3{display:flex;align-items:center;gap:6px;font-family:var(--head);font-weight:600;font-size:16px;color:var(--ink);height:22px}
.feature .icon{width:20px;height:20px;border-radius:50%;background:var(--red)}
.feature .shot{width:166px;height:73px;margin-top:4px;box-shadow:0 2px 3px rgba(0,0,0,.2)}
.feature p{font-size:9px;line-height:11.5px;color:var(--body);margin:9px 4px 0;height:46px;overflow:hidden}
.more{display:inline-flex;align-items:center;gap:5px;margin-top:10px;height:19px;padding:0 8px;background:linear-gradient(var(--red),var(--red-dark));color:#fff;font-size:8px;font-weight:600;border-radius:2px}
.more b{width:9px;height:9px;border-radius:50%;background:#fff;display:inline-block;position:relative}
.more b::after{content:"";position:absolute;left:2.5px;top:2.5px;border-left:4px solid var(--red);border-top:2px solid transparent;border-bottom:2px solid transparent}

/* text sections */
.section-title{left:0;width:714px;text-align:center;font-family:var(--head);font-weight:600;font-size:17px;color:var(--ink)}
.welcome-copy{left:62px;top:577px;width:590px;text-align:center;font-size:8.6px;line-height:12.5px;color:var(--body)}
.welcome-copy p+p{margin-top:12px}
.welcome-copy .view-more{display:block;margin-top:8px;color:var(--red)}

.how{left:0;top:683px;width:714px;height:162px;background:linear-gradient(#161618,#242426 60%,#1b1b1d)}
.how-copy{left:62px;top:740px;width:590px;text-align:center;font-size:8.6px;line-height:12.5px;color:#f0f0f0}
.how-copy .view-more{display:block;margin-top:12px;color:#fff}

.get-copy{left:60px;top:912px;width:370px;font-size:8.6px;line-height:12.5px;color:var(--body)}
.get-copy p+p{margin-top:12px}
.get-photo{left:441px;top:913px;width:214px;height:100px;background:linear-gradient(90deg,#e9eaed,#d8d4cf 55%,#c9c7c6)}

/* footer */
.footer{left:0;top:1056px;width:714px;height:116px;background:var(--footer)}
.foot-brand{left:62px;top:1080px;display:flex;align-items:center;gap:6px;font-family:var(--head);font-weight:600;font-size:21px;color:#cfcfcf}
.foot-brand .brand-dot{width:30px;height:30px;background:#8d8d8d}
.social{left:114px;top:1131px;display:flex;gap:6px}
.social i{width:10px;height:10px;background:#e6e6e6;border-radius:2px;display:block}
.foot-head{top:1076px;font-family:var(--head);font-weight:600;font-size:10px;color:#fff}
.address{left:256px;top:1104px;display:flex;gap:5px;font-size:8.5px;line-height:11px;color:#eee}
.address .txt{border-left:1px solid #666;padding-left:8px;width:105px}
.phone{left:389px;top:1104px;display:flex;gap:5px;font-size:8.5px;color:#eee;align-items:center}
.phone .txt{border-left:1px solid #666;padding-left:8px;height:22px;line-height:14px}
.news-note{left:510px;top:1094px;font-size:7px;color:#9a9a9a}
.news-input{left:509px;top:1110px;width:146px;height:18px;background:#fff;font-size:7px;color:#999;padding:5px 6px}
.submit{left:610px;top:1137px;width:45px;height:16px;background:linear-gradient(var(--red),var(--red-dark));color:#fff;font-size:8px;font-weight:600;text-align:center;line-height:16px;border-radius:2px}
.bottom{left:0;top:1172px;width:714px;height:28px;background:var(--red);color:#fff;font-size:7.5px}
.bottom .copy{position:absolute;left:61px;top:11px}
.bottom .mail{position:absolute;left:572px;top:10px;display:flex;align-items:center;gap:5px}
</style>
</head>
<body>
<div class="page">

  <div class="abs topline"></div>
  <header class="abs header"></header>
  <a class="abs brand" href="#"><span class="brand-dot"></span>ThreadKove</a>
  <div class="abs search">Search
    <svg width="11" height="11" viewBox="0 0 11 11"><circle cx="4.5" cy="4.5" r="3.3" fill="none" stroke="#222" stroke-width="1.5"/><line x1="7" y1="7" x2="10" y2="10" stroke="#222" stroke-width="1.8"/></svg>
  </div>
  <div class="abs account"><a href="#">Login</a><span>|</span><a href="#">Register</a></div>
  <nav class="abs nav"><a href="#">Enterprise</a><a href="#">Pricing</a><a href="#">Support &amp; Learning</a><a href="#">Company</a></nav>

  <section class="abs hero" role="img" aria-label="Dim photo of hands holding a tablet with an investigation app beside a coffee cup, seen through a magnifying glass"></section>
  <h1 class="abs hero-title">INVESTIGATION<br>WEB APPLICATION</h1>
  <p class="abs hero-copy">that would organize, create visualizations and allow collaboration. Aenean ut felis quis lectus viverra varius. Nunc iaculis odio vel tortor scelerisque</p>
  <a class="abs btn-hero" href="#">Click here to Learn More</a>
  <div class="abs dots"><i></i><i></i><i></i></div>
  <svg class="abs arrow-l" width="20" height="50" viewBox="0 0 20 50"><polyline points="18,1 2,25 18,49" fill="none" stroke="#c23a2a" stroke-width="1.5"/></svg>
  <svg class="abs arrow-r" width="20" height="50" viewBox="0 0 20 50"><polyline points="2,1 18,25 2,49" fill="none" stroke="#c23a2a" stroke-width="1.5"/></svg>

  <section class="abs features"></section>
  <article class="abs feature" style="left:68px">
    <h3><span class="icon"></span>Organize</h3>
    <div class="shot" role="img" aria-label="Photo of paper files laid out in rows on a table" style="background:linear-gradient(#8a5a3c,#b98b66 50%,#e8dccb)"></div>
    <p>ThreadKove is an on-line system that allows you to enter what you know about a person, event, object, or group. Who are their friends – and who are their enemies? ...</p>
    <a class="more" href="#">more <b></b></a>
  </article>
  <article class="abs feature" style="left:277px">
    <h3><span class="icon"></span>Visualize</h3>
    <div class="shot" role="img" aria-label="Screenshot of a data analysis tool with a bar timeline" style="background:linear-gradient(#f2f2f2 55%,#7c97b3)"></div>
    <p>Once data has been entered, use ThreadKove's graphical analysis tools to analyze your data in new ways. Aliquam interdum sed ante non posuere...</p>
    <a class="more" href="#">more <b></b></a>
  </article>
  <article class="abs feature" style="left:486px">
    <h3><span class="icon"></span>Colaborate</h3>
    <div class="shot" role="img" aria-label="Laptop with floating translucent screens on a cyan background" style="background:linear-gradient(120deg,#d9f1f5,#7fc9d9 50%,#cfe9ee)"></div>
    <p>Nullam vel sem molestie, ornare metus in, ultricies nibh. Praesent ac sem a justo dapib us dapibus ac et elit. Aliquam interdum sed ante non posuere.</p>
    <a class="more" href="#">more <b></b></a>
  </article>

  <h2 class="abs section-title" style="top:536px">Welcome to ThreadKove</h2>
  <div class="abs welcome-copy">
    <p>Have you ever compiled a lot of data about something, but been unable to figure out what it means? Often, the number of people involved, the number of events at which they might have met, and the number of common contacts are just too much for a person to track. This can happen when you are trying to understand the players and interests in current events, or the characters and actions in a novel. It's easy to collect the data, but hard to visualize it or analyze the relationships.</p>
    <p>This is where ThreadKove comes in. ThreadKove allows you to easily visualize people, events, things, groups, and timelines and to easily see the relationships between them.</p>
    <a class="view-more" href="#">View more »</a>
  </div>

  <section class="abs how" role="img" aria-label="Dark band with faint rows of scattered numbers"></section>
  <h2 class="abs section-title" style="top:710px;color:var(--white)">How does ThreadKove work?</h2>
  <div class="abs how-copy">
    <p>Once data has been entered, use ThreadKove's graphical analysis tools to analyze your data in new ways. Use relationship maps to find out how two people or groups are associated. Use timeline analysis to show cause and effect of seemingly unrelated events. Use social network mapping to show how relationships change over time. Look for events that stand out or relationships that have great impact on multiple events. Like a spider's web, look for the intersections that matter, then look for the players that brought that intersection into focus.</p>
    <a class="view-more" href="#">View more »</a>
  </div>

  <h2 class="abs section-title" style="top:876px">What do I get with ThreadKove?</h2>
  <div class="abs get-copy">
    <p>Basic ThreadKove will allow any registered user to create, maintain and analyze one investigation. Advanced features will be available a la carte and will include special analytical reports, multiple investigations, and the ability to share an investigation among multiple users. Investigations of general interest could also be shared publicly in read-only mode.</p>
    <p>You will also get access to several read-only public investigations to use as a model. These might include the plots of popular novels or movies, the details of a major political event, or an investigation into a famous crime.</p>
  </div>
  <div class="abs get-photo" role="img" aria-label="Photo of a woman working at a laptop in a bright office"></div>

  <footer class="abs footer"></footer>
  <a class="abs foot-brand" href="#"><span class="brand-dot"></span>ThreadKove</a>
  <div class="abs social" aria-label="Social links"><i></i><i></i><i></i><i></i></div>

  <h4 class="abs foot-head" style="left:259px">Contact Info</h4>
  <div class="abs address">
    <svg width="10" height="22" viewBox="0 0 10 22"><path d="M5 3 L10 8 H8.5 V13 H1.5 V8 H0 Z" fill="#eee"/></svg>
    <span class="txt">345-Aenean ut felis quis viverra varius. Nunc iaculis</span>
  </div>
  <div class="abs phone">
    <svg width="10" height="22" viewBox="0 0 10 22"><path d="M2 3 C1 4 1 7 3.5 10 C6 13 8 13 9 12 L7.5 10 L6 10.8 C5 10.3 3.5 8.5 3.3 7.5 L4.2 6.3 Z" fill="#eee"/></svg>
    <span class="txt">+45 00 11 22 33</span>
  </div>

  <h4 class="abs foot-head" style="left:510px">Subscribe Newsletter</h4>
  <p class="abs news-note">Curabitur tempor posuere Fermentum. Sed</p>
  <div class="abs news-input">Enter email address</div>
  <a class="abs submit" href="#">Submit</a>

  <div class="abs bottom">
    <span class="copy">Copyright © 2014 all rights reserved.</span>
    <span class="mail">
      <svg width="10" height="7" viewBox="0 0 10 7"><rect width="10" height="7" fill="#fff"/><polyline points="0,0 5,4 10,0" fill="none" stroke="#d8321c" stroke-width="1"/></svg>
      info@threadkove.example
    </span>
  </div>

</div>
</body>
</html>
```